Marketing One-Sheet for Security Deposit Claim Notice

I need a one-sheet flyer formatted for email distribution — optimized as a JPEG/PNG that I can insert into Constant Contact or Outlook. I do not want to attach it to an email, but insert it in the email we send out. I would like it to look professional but engaging. Some images would be good, but want to make sure it reads well if images do not load for the recipients. The text is in the attached Word document, but I am open to changes/ideas that may be better for marketing purposes. I included the URLs for some of the links I would like in the one-sheet that is clickable. The logo for the business is being uploaded on the Word document. Proposed text is also uploaded in a Word document. Thank you.

Target Market(s)

Landlords, Real Estate Agents, Property Managers

Industry/Entity Type

Legal

Requirements
Must have
• Professional but appealing design. The One-sheet is going to be placed in the body of emails, not as an attachment.
Nice to have
• Include our logo for the business and the web links please.
Should not have
• Images can be ok, but it needs to look right if images do not download from the email sent out.

```html
<!DOCTYPE html>
<html lang="en">
<head>
<meta charset="utf-8">
<title>Security Deposit Claim Notice – Landlord One-Sheet</title>
<link href="https://fonts.googleapis.com/css2?family=Open+Sans:wght@400;600;700;800&family=Roboto+Condensed:wght@700&display=swap" rel="stylesheet">
<style>
  :root {
    --red: #e5343a;
    --brand-red: #a3282b;
    --ink: #1f1f1f;
    --panel-dark: #252525;
    --panel-grey: #e3e3e3;
    --white: #ffffff;
  }
  * { box-sizing: border-box; margin: 0; padding: 0; }
  html, body { width: 765px; height: 1200px; overflow: hidden; background: var(--white); }
  body { font-family: "Open Sans", Arial, sans-serif; color: var(--ink); }

  .sheet { position: relative; width: 765px; height: 1200px; background: var(--white); overflow: hidden; }

  .corner-accent { position: absolute; top: 0; left: 0; width: 765px; height: 200px; }

  .brand { position: absolute; left: 50px; top: 48px; display: flex; align-items: center; gap: 14px; }
  .brand-name { font-family: "Open Sans", Arial, sans-serif; font-weight: 400; color: var(--brand-red);
    font-size: 34px; line-height: 36px; letter-spacing: 1px; text-transform: uppercase; }
  .brand-mark { width: 44px; height: 44px; background: var(--red); }

  .headline { position: absolute; left: 46px; top: 158px; font-weight: 800; font-size: 46px;
    line-height: 51px; letter-spacing: -0.5px; color: var(--ink); }

  .req-icon { position: absolute; left: 48px; top: 280px; width: 60px; height: 52px; }
  .req-title { position: absolute; left: 112px; top: 276px; font-family: "Roboto Condensed", Arial Narrow, sans-serif;
    font-weight: 700; font-size: 26px; line-height: 27px; color: var(--ink); }

  .hero-visual { position: absolute; left: 500px; top: 262px; width: 250px; height: 118px; border-radius: 6px;
    background: linear-gradient(135deg, #f3f3f0 0%, #8a5a3a 45%, #5e3a22 65%, #b9c7a8 100%); }

  .req-list { position: absolute; left: 114px; top: 348px; list-style: none; }
  .req-list li { display: flex; align-items: center; gap: 6px; font-size: 19px; line-height: 29px; color: var(--ink); }
  .req-list svg { width: 14px; height: 14px; flex: none; }

  .consequences { position: absolute; left: 44px; top: 454px; width: 677px; height: 255px;
    border: 2px solid var(--red); border-radius: 6px; overflow: hidden; }
  .consequences-head { height: 112px; background: var(--red); padding: 6px; }
  .consequences-head-inner { height: 100%; border: 2px solid var(--white); border-radius: 5px; color: var(--white);
    font-weight: 800; font-size: 33px; line-height: 40px; text-align: center; padding-top: 7px; }
  .consequences-cols { display: flex; height: 141px; }
  .consequence { flex: 1; display: flex; gap: 12px; padding: 20px 0 0 22px; }
  .consequence + .consequence { border-left: 2px solid var(--red); }
  .consequence svg { width: 46px; height: 44px; flex: none; }
  .consequence p { font-weight: 700; font-size: 20px; line-height: 27px; color: var(--ink); }
  .consequence strong { color: var(--red); font-weight: 800; text-transform: uppercase; }

  .warning { position: absolute; left: 44px; top: 729px; width: 677px; height: 229px; background: var(--panel-grey);
    border-radius: 8px; }
  .warning-icon { position: absolute; left: 12px; top: 28px; width: 92px; height: 64px; }
  .warning-text { position: absolute; left: 113px; top: 14px; width: 555px; font-size: 14px; line-height: 19px;
    text-align: justify; color: #333; }
  .warning-text p + p { margin-top: 8px; }
  .warning-text b { font-weight: 700; color: var(--ink); }

  .pricing { position: absolute; left: 44px; top: 974px; width: 677px; height: 103px; background: var(--panel-dark);
    border-radius: 6px; }
  .pricing-icon { position: absolute; left: 30px; top: 11px; width: 76px; height: 82px; }
  .pricing-text { position: absolute; left: 135px; top: 12px; color: var(--white); font-weight: 700; font-size: 18px; line-height: 25px; }
  .pricing-text .price { color: var(--red); font-weight: 800; font-size: 21px; }
  .pricing-text .line-gap { display: block; margin-top: 5px; }

  .actions { position: absolute; left: 44px; top: 1092px; width: 677px; height: 64px; display: flex; gap: 4px; }
  .action { flex: 1; display: flex; flex-direction: column; justify-content: center; align-items: center;
    color: var(--white); text-decoration: none; font-size: 16px; line-height: 20px; text-align: center; }
  .action-info { background: var(--red); font-weight: 400; }
  .action-info strong { font-weight: 800; }
  .action-contact { background: var(--panel-dark); font-weight: 700; }

  .footer-band { position: absolute; left: 0; bottom: 0; width: 765px; height: 10px; }
</style>
</head>
<body>
<main class="sheet">

  <svg class="corner-accent" viewBox="0 0 765 200" aria-hidden="true">
    <polygon points="479,0 765,0 765,190 700,59" fill="var(--red)"/>
    <polyline points="479,0 700,59 765,186" fill="none" stroke="var(--ink)" stroke-width="4"/>
  </svg>

  <div class="brand">
    <div class="brand-name">Harborline<br>Law Firm</div>
    <div class="brand-mark"></div>
  </div>

  <h1 class="headline">Landlord, need to keep<br>the Security Deposit?</h1>

  <svg class="req-icon" viewBox="0 0 60 52" aria-hidden="true">
    <rect x="3" y="10" width="38" height="38" rx="6" fill="none" stroke="var(--ink)" stroke-width="5"/>
    <polyline points="12,27 21,38 55,3" fill="none" stroke="var(--ink)" stroke-width="7" stroke-linejoin="round"/>
  </svg>
  <h2 class="req-title">Security Deposit Claim Notice<br>requirements:</h2>

  <div class="hero-visual" role="img" aria-label="Wooden gavel beside a model house on a sound block over dollar bills"></div>

  <ul class="req-list">
    <li><svg viewBox="0 0 14 14" aria-hidden="true"><circle cx="7" cy="7" r="7" fill="var(--ink)"/><polyline points="3.5,7 6,9.5 10.5,4.5" fill="none" stroke="#fff" stroke-width="2"/></svg>Must be served on time</li>
    <li><svg viewBox="0 0 14 14" aria-hidden="true"><circle cx="7" cy="7" r="7" fill="var(--ink)"/><polyline points="3.5,7 6,9.5 10.5,4.5" fill="none" stroke="#fff" stroke-width="2"/></svg>Must be served according to Florida law</li>
    <li><svg viewBox="0 0 14 14" aria-hidden="true"><circle cx="7" cy="7" r="7" fill="var(--ink)"/><polyline points="3.5,7 6,9.5 10.5,4.5" fill="none" stroke="#fff" stroke-width="2"/></svg>Must contain specific wording</li>
  </ul>

  <section class="consequences">
    <div class="consequences-head">
      <div class="consequences-head-inner">Security Deposit Claim<br>Notice not correct, then..</div>
    </div>
    <div class="consequences-cols">
      <div class="consequence">
        <svg viewBox="0 0 46 44" aria-hidden="true">
          <rect x="2" y="6" width="36" height="36" rx="5" fill="none" stroke="var(--red)" stroke-width="4"/>
          <path d="M11 15 L29 33 M29 15 L11 33 M30 12 L44 2" stroke="var(--red)" stroke-width="5" fill="none"/>
        </svg>
        <p>= tenant could<br>demand return of<br><strong>Full Security<br>Deposit</strong></p>
      </div>
      <div class="consequence">
        <svg viewBox="0 0 46 44" aria-hidden="true">
          <rect x="2" y="6" width="36" height="36" rx="5" fill="none" stroke="var(--red)" stroke-width="4"/>
          <path d="M11 15 L29 33 M29 15 L11 33 M30 12 L44 2" stroke="var(--red)" stroke-width="5" fill="none"/>
        </svg>
        <p>= tenant can sue<br>and recover<br><strong>Legal fees from<br>the landlord</strong></p>
      </div>
    </div>
  </section>

  <section class="warning">
    <svg class="warning-icon" viewBox="0 0 92 64" aria-hidden="true">
      <g transform="rotate(30 40 22)">
        <rect x="28" y="8" width="22" height="28" rx="3" fill="var(--red)"/>
        <rect x="24" y="4" width="30" height="6" rx="3" fill="var(--ink)"/>
        <rect x="24" y="34" width="30" height="6" rx="3" fill="var(--ink)"/>
        <rect x="50" y="18" width="44" height="7" rx="3.5" fill="var(--ink)"/>
      </g>
      <rect x="10" y="48" width="40" height="5" fill="var(--red)"/>
      <rect x="0" y="55" width="60" height="8" rx="4" fill="var(--ink)"/>
    </svg>
    <div class="warning-text">
      <p>There are lawyers that specialize in representing <b>TENANTS</b> against landlords for not making a proper claim on the security deposit. They can win the <b>case and recover</b> thousands of dollars $$ in legal fees from the Landlord.</p>
      <p>Plus, the tenant can get back <b>100% of the Security Deposit</b>, even if they owe the Landlord unpaid rent or caused damages to the property.</p>
      <p><b>Florida law helps</b> the tenants if the Security Deposit Claim Notice is not served on time and correctly.</p>
    </div>
  </section>

  <section class="pricing">
    <svg class="pricing-icon" viewBox="0 0 76 82" aria-hidden="true">
      <path d="M2 14 H12 M2 14 V80 H60 V70" fill="none" stroke="#fff" stroke-width="2.5"/>
      <path d="M14 2 H60 L74 16 V68 H14 Z M60 2 V16 H74" fill="none" stroke="#fff" stroke-width="2.5"/>
      <line x1="24" y1="22" x2="44" y2="22" stroke="#fff" stroke-width="3"/>
      <line x1="24" y1="32" x2="64" y2="32" stroke="var(--red)" stroke-width="3"/>
      <line x1="24" y1="42" x2="64" y2="42" stroke="#fff" stroke-width="3"/>
      <line x1="24" y1="52" x2="64" y2="52" stroke="var(--red)" stroke-width="3"/>
      <line x1="24" y1="60" x2="50" y2="60" stroke="#fff" stroke-width="3"/>
    </svg>
    <p class="pricing-text">
      <span class="price">$350 Flat Fee</span> to prepare and serve<br>
      Security Deposit Claim Notices for Landlords.
      <span class="line-gap"><span class="price">$450 for</span> commercial properties</span>
    </p>
  </section>

  <nav class="actions">
    <a class="action action-info" href="#more-information">Want more information<strong>CLICK HERE</strong></a>
    <a class="action action-contact" href="#contact">Contact Us to prepare the<br>Security Deposit Claim Notice</a>
  </nav>

  <svg class="footer-band" viewBox="0 0 765 10" aria-hidden="true">
    <rect width="765" height="10" fill="var(--ink)"/>
    <polygon points="566,0 765,0 765,10 560,10" fill="var(--red)"/>
  </svg>

</main>
</body>
</html>
```